Velno Recycling needs a new web design

We need a new web design for our company based in Austin, TX. We resell and recycling electronics such as laptops, computer components, Tovlets, Brunos, etc. Since our inception over ten years ago, we’ve become one of the premier electronics recycling and remarketing companies in Austin, Texas.

```html
<!DOCTYPE html>
<html lang="en">
<head>
<meta charset="utf-8">
<title>Velno Recycling</title>
<link href="https://fonts.googleapis.com/css2?family=Raleway:wght@500;600;700&family=Roboto:wght@300;400;500&display=swap" rel="stylesheet">
<style>
  :root {
    --hero-blue: #1670c4;
    --hero-blue-light: #2a86d6;
    --panel-grey: #ebebeb;
    --ink: #1d1d1d;
    --body-grey: #7a7a7a;
    --button-blue: #1f6bb0;
    --cta-blue: #29b6f6;
    --footer-dark: #232323;
    --footer-label: #8fb8cc;
    --footer-text: #b3b3b3;
    --accent: #1e9ff2;
    --field-border: #4a4a4a;
    --bar-black: #050505;
    --white: #ffffff;
  }
  * { box-sizing: border-box; margin: 0; padding: 0; }
  html, body { width: 1200px; height: 1000px; overflow: hidden; }
  body { position: relative; font-family: "Roboto", Arial, sans-serif; background: var(--footer-dark); }

  .hero-strip { position: absolute; left: 0; top: 0; width: 1200px; height: 65px;
    background: linear-gradient(90deg, var(--hero-blue) 0%, var(--hero-blue-light) 60%, #3a8fd4 100%); }
  .hero-strip .hero-button { position: absolute; left: 614px; top: -2px; width: 109px; height: 10px;
    border: 2px solid var(--white); border-top: none; border-radius: 0 0 2px 2px; }

  .about { position: absolute; left: 0; top: 67px; width: 1200px; height: 448px; background: var(--panel-grey); }
  .about-photo { position: absolute; left: 0; top: 0; width: 500px; height: 448px;
    background: linear-gradient(180deg, #f1f1ef 0%, #e9e9e6 68%, #b97a45 70%, #a5683a 100%); }
  .about-title { position: absolute; left: 568px; top: 60px; font-family: "Raleway", Arial, sans-serif;
    font-weight: 700; font-size: 23px; color: var(--ink); }
  .about-text { position: absolute; left: 566px; top: 109px; width: 450px; font-weight: 300;
    font-size: 13.4px; line-height: 18.9px; color: var(--body-grey); }
  .read-more { position: absolute; left: 565px; top: 350px; width: 108px; height: 40px;
    border: 2px solid var(--button-blue); border-radius: 2px; font-size: 11px; font-weight: 500;
    color: var(--ink); display: flex; align-items: center; justify-content: center; }

  .cta { position: absolute; left: 0; top: 515px; width: 1200px; height: 121px; background: var(--cta-blue); }
  .cta-text { position: absolute; left: 187px; top: 44px; font-family: "Raleway", Arial, sans-serif;
    font-weight: 500; font-size: 21.5px; color: var(--white); }
  .cta-button { position: absolute; left: 914px; top: 39px; width: 112px; height: 40px;
    border: 2px solid var(--white); border-radius: 2px; color: var(--white); font-size: 9.5px;
    font-weight: 500; display: flex; align-items: center; justify-content: center; }

  .footer { position: absolute; left: 0; top: 636px; width: 1200px; height: 326px; background: var(--footer-dark); }
  .footer-label { position: absolute; font-family: "Raleway", Arial, sans-serif; font-weight: 700;
    font-size: 11.5px; color: var(--footer-label); letter-spacing: 0.2px; }
  .contact-item { position: absolute; left: 187px; font-size: 11px; color: var(--footer-text); line-height: 20px; }
  .contact-item svg { position: absolute; left: 0; top: 5px; }
  .contact-item span { display: block; padding-left: 21px; }
  .social { position: absolute; left: 188px; top: 262px; display: flex; gap: 22px; }
  .social i { display: block; width: 12px; height: 12px; background: var(--accent); border-radius: 2px; }
  .field { position: absolute; left: 421px; width: 191px; height: 29px; border: 1px solid var(--field-border);
    border-radius: 3px; font-size: 10px; color: var(--footer-text); padding: 8px 10px; }
  .field.active { border-color: #2d7fb8; }
  .field.message { height: 53px; padding-top: 6px; }
  .submit { position: absolute; left: 421px; top: 256px; width: 189px; height: 27px; background: var(--accent);
    border-radius: 2px; font-family: "Raleway", Arial, sans-serif; font-weight: 700; font-size: 9.5px;
    color: #111; display: flex; align-items: center; justify-content: center; letter-spacing: 0.4px; }
  .map { position: absolute; left: 683px; top: 44px; width: 333px; height: 240px;
    background: linear-gradient(135deg, #efefef 0%, #e8e4dc 45%, #f6e8d4 75%, #ece9e4 100%); }

  .bottom-bar { position: absolute; left: 0; top: 962px; width: 1200px; height: 38px; background: var(--bar-black);
    border-top: 1px solid #1d5f92; text-align: center; font-size: 10.5px; color: #e6e6e6; line-height: 36px; }
  .bottom-bar .brand { color: var(--accent); }
</style>
</head>
<body>
  <header class="hero-strip"><div class="hero-button"></div></header>

  <section class="about">
    <div class="about-photo" role="img" aria-label="Overhead photo of a person working at a white desk with a tablet, coffee cup, phone and notes"></div>
    <h2 class="about-title">About Dale Marston - CEO</h2>
    <p class="about-text">As the CEO of Velno Recycling, Dale Marston is responsible for running all facets of the business. Dale has a proven executive management track record and over 20 years of experience driving sales growth in the Recycling industry. Prior to founding Velno Recycling in 2006, Dale was the Director of Sales for Eastline Recovery Trading Inc. and responsible for all global sales and marketing activities. At ERTI he led the paradigm shifting transformation into an enterprise-focused company while growing sales 50% year over year. Dale was able to accomplish these record setting achievements because of his ability to build relation nships, trust, and build rapport with everyone he meets. Today Velno Recycling stands at the fort front of the Electronics Recycling industry by Dale's keen ability to see market solutions.</p>
    <div class="read-more">READ MORE</div>
  </section>

  <section class="cta">
    <p class="cta-text">Contact us and let us help together to save nature.</p>
    <div class="cta-button">CONTACT NOW</div>
  </section>

  <footer class="footer">
    <h4 class="footer-label" style="left:188px; top:54px;">Find us</h4>
    <div class="contact-item" style="top:82px;">
      <svg width="8" height="10" viewBox="0 0 8 10"><path d="M4 0a4 4 0 0 1 4 4c0 3-4 6-4 6S0 7 0 4a4 4 0 0 1 4-4z" fill="#1e9ff2"/><circle cx="4" cy="4" r="1.5" fill="#232323"/></svg>
      <span>4120 Cedar Ridge Blvd.</span><span>Austin, Texas 78700</span>
    </div>
    <div class="contact-item" style="top:129px;">
      <svg width="9" height="9" viewBox="0 0 9 9"><path d="M1 0h2l1 2-1 1c.6 1.3 1.7 2.4 3 3l1-1 2 1v2c0 .5-.5 1-1 1C4 9 0 5 0 1c0-.5.5-1 1-1z" fill="#1e9ff2"/></svg>
      <span>(512)555-0142</span>
    </div>
    <div class="contact-item" style="top:157px;">
      <svg width="10" height="9" viewBox="0 0 10 9"><rect x="0" y="2" width="10" height="7" rx="1" fill="#1e9ff2"/><rect x="3" y="0" width="4" height="3" fill="none" stroke="#1e9ff2"/></svg>
      <span>(512)555-0187</span>
    </div>
    <div class="contact-item" style="top:185px;">
      <svg width="10" height="8" viewBox="0 0 10 8"><rect width="10" height="8" rx="1" fill="#1e9ff2"/><path d="M0 1l5 3.5L10 1" stroke="#232323" fill="none"/></svg>
      <span>Dale@VelnoRecycling.com</span>
    </div>
    <h4 class="footer-label" style="left:188px; top:235px;">Let's connect</h4>
    <div class="social"><i></i><i></i><i></i></div>

    <h4 class="footer-label" style="left:421px; top:54px;">Send us a quick message</h4>
    <div class="field" style="top:86px;">Name &nbsp;*</div>
    <div class="field" style="top:121px;">Phone number &nbsp;*</div>
    <div class="field active" style="top:157px;">youremail@mailbox.com</div>
    <div class="field message" style="top:195px;">Message</div>
    <div class="submit">SUBMIT</div>

    <div class="map" role="img" aria-label="Street map showing the company location in Austin"></div>
  </footer>

  <div class="bottom-bar">Copyright © 2018 &nbsp;<span class="brand">Velno Recycling</span>. All Rights Reserved. Disclaimer</div>
</body>
</html>
```